Green Logistics / Last Mile Delivery Firm needs cool one-page website

FYI - We do have a detailed brief in the uploaded files section below
COMPANY
We recently launched the company Quillby Logistics which is a pioneer in urban green logistics and provides zero-emissions last mile delivery services (i.e. delivery of parcels with delivery vans to the doorstep of households) for its logistics and retail clients.
We take on urban parcel delivery for our clients with a 100% electric commercial vehicles fleet, fair and sustainable working conditions for our employees and an unparalleled professional and customer-focused mindset.
WEBSITE
In the detailed brief, we have provided examples to emulate. We need the design + coding of the website. Website needs to be friendly/optimized for and should open swiftly on both Android & iOS.
In general, the website should convey
- green mission of the company
- sustainability (good working conditions, focus on employees)
- customer orientation
- professionalism
DESIGN
In the detailed brief, we have provided designs to emulate.
Color design: we do have a logo which features 2 green colors (one lighter and one darker color tone). However, the colors on the website do not necessarily need to follow these 2 colors exactly as we are able to switch the logo colors.
Imagery: should reflect maybe 50% green/leaf/tree , 25% customer and employee orientation, and 25% logistics (here it's important that it is the last mile delivery, i.e. delivery with delivery vans to the doorstep of households)

```html
<!DOCTYPE html>
<html lang="en">
<head>
<meta charset="utf-8">
<title>Quillby Logistics – Sustainable Last Mile</title>
<link rel="stylesheet" href="https://fonts.googleapis.com/css2?family=Montserrat:wght@500;600;700&family=Open+Sans:wght@400;600;700&display=swap">
<style>
:root{
  --green:#1f9a45;
  --green-dark:#17773a;
  --ink:#2b2b2b;
  --muted:#6b6b6b;
  --band:#ececec;
  --forest:#1e3a22;
  --footer:#1d1d1d;
  --footer-deep:#111;
  --white:#fff;
}
*{box-sizing:border-box;margin:0;padding:0}
html,body{width:1200px;height:1200px;overflow:hidden;background:var(--white)}
body{font-family:"Open Sans",sans-serif;color:var(--ink)}
.stage{position:absolute;left:0;top:0;width:1932px;height:1932px;transform:scale(.62112);transform-origin:0 0}
.page{position:absolute;left:760px;top:28px;width:412px;height:1876px;background:var(--white);overflow:hidden}
section,header,footer{position:absolute;left:0;width:412px}
.abs{position:absolute}
h2.section-title{font-family:"Montserrat",sans-serif;font-weight:700;font-size:11px;color:var(--ink);letter-spacing:.2px}
h2.section-title span{color:var(--green)}
.rule{position:absolute;width:16px;height:1px;background:var(--green)}
.tiny{font-size:4.4px;line-height:7.6px;color:var(--muted)}
.btn{position:absolute;background:var(--green);color:var(--white);font-family:"Montserrat",sans-serif;font-weight:600;font-size:4.2px;border-radius:8px;display:flex;align-items:center;justify-content:center;letter-spacing:.2px}
.icon-ring{position:absolute;border-radius:50%;display:flex;align-items:center;justify-content:center}

/* hero */
.hero{top:0;height:196px;background:radial-gradient(ellipse at 50% 45%,#4f6b34 0%,#2c4521 45%,#152512 100%)}
.brand{position:absolute;display:flex;align-items:center;gap:3px;font-family:"Montserrat",sans-serif;font-weight:700;color:var(--green)}
.brand i{display:block;border-radius:50%;background:var(--green)}
.nav{position:absolute;right:42px;top:15px;display:flex;gap:12px;font-family:"Montserrat",sans-serif;font-weight:600;font-size:3.8px;color:var(--white)}
.nav .active{border-bottom:1px solid var(--white)}
.hero h1{position:absolute;left:38px;top:73px;font-family:"Montserrat",sans-serif;font-weight:700;font-size:14.5px;color:var(--white)}
.hero .lead{position:absolute;left:38px;top:93px;font-size:8.2px;color:#e8f0e3}
.arrow{position:absolute;top:100px;width:17px;height:17px;border-radius:50%}

/* about */
.about{top:196px;height:307px}
.about-photo{left:38px;top:31px;width:162px;height:276px;background:linear-gradient(180deg,#a9c6d6 0%,#d7dccb 35%,#6f7d42 60%,#3e4a2b 100%)}
.about-item h3{font-family:"Montserrat",sans-serif;font-weight:500;font-size:7px;color:var(--ink);margin-bottom:2px}
.about-item p{margin-bottom:4px}
.line-icon{border:1px solid #cfe6d6;width:20px;height:20px;background:var(--white)}

/* is / is not */
.compare{top:503px;height:143px;background:var(--band)}
.compare h2{position:absolute;top:14px;width:100%;text-align:center;font-family:"Montserrat",sans-serif;font-weight:500;font-size:8.5px}
.fill-ring{background:var(--green);width:24px;height:24px}
.not-list{position:absolute;right:212px;top:68px;text-align:right}
.not-list li,.is-list li{list-style:none;font-size:4.4px;height:10.8px;line-height:10.8px}
.not-list li{color:var(--green);text-decoration:line-through}
.not-list li::before{content:"";display:inline-block;width:18px;height:.5px;background:var(--green);vertical-align:middle;margin-right:1px}
.is-list{position:absolute;left:210px;top:68px;color:var(--muted)}
.divider{position:absolute;left:205px;top:68px;width:.6px;height:60px;background:#c4c4c4}

/* services */
.services{top:646px;height:198px}
.leaves{background:linear-gradient(160deg,#2f7a2a,#5aa63a 60%,rgba(255,255,255,0))}
.card{position:absolute;top:106px;width:77px;height:75px;background:var(--white);box-shadow:0 0 3px rgba(0,0,0,.12);text-align:center;padding:22px 6px 0}
.card h4{font-family:"Montserrat",sans-serif;font-weight:500;font-size:4.6px;line-height:6px;color:var(--ink);margin-bottom:2px}
.card p{font-size:4px;line-height:6.4px;color:var(--muted)}
.card .icon-ring{left:29px;top:-4px;width:18px;height:18px;background:var(--green)}

/* cta bands */
.touch{top:844px;height:114px;background:radial-gradient(ellipse at 40% 50%,#2f5530,#1a311b 60%,#0f1d10)}
.cta-title{position:absolute;font-family:"Montserrat",sans-serif;font-weight:600;font-size:11.5px;color:var(--white)}
.cta-text{position:absolute;font-size:5px;line-height:9px;color:var(--white);font-weight:600}
.interest{top:1424px;height:105px;background:radial-gradient(ellipse at 50% 40%,#3da046,#23862f 60%,#176f24)}

/* careers */
.careers{top:958px;height:466px}
.careers-text p{font-size:4.4px;line-height:7.8px;color:var(--ink);margin-bottom:7px}
.careers-photo{left:211px;top:19px;width:162px;height:178px;background:linear-gradient(180deg,#5b5a58 0%,#8b7f6d 45%,#2c3b5a 70%,#b58c5a 100%)}
.accordion{left:86px;top:217px;width:220px;height:218px;background:#eeeeee}
.acc-head{position:absolute;left:0;top:0;width:220px;height:17px;background:var(--green);color:var(--white);font-family:"Montserrat",sans-serif;font-weight:700;font-size:4.5px;display:flex;align-items:center;justify-content:space-between;padding:0 8px}
.acc-box{position:absolute;left:20px;width:180px;background:var(--white);border:.8px solid #7fc596}
.acc-row{height:19px;display:flex;align-items:center;justify-content:space-between;padding:0 9px;font-size:4.2px;color:var(--ink)}
.acc-row b{color:var(--green);font-size:6px;font-weight:700}
.acc-body{padding:7px 19px 0;font-size:4.2px;line-height:7px;color:var(--muted)}
.acc-body p{margin-bottom:3px}

/* contact */
.contact{top:1529px;height:286px}
.field-label{position:absolute;left:38px;font-size:4.2px;color:var(--ink)}
.field{position:absolute;left:38px;background:#efefef;border:.6px solid #cfcfcf}
.info{position:absolute;left:211px;display:flex;align-items:center;gap:6px;font-size:4.2px;color:var(--ink)}

/* footer */
.footer{top:1815px;height:61px;background:var(--footer)}
.footer-nav{position:absolute;left:132px;top:17px;display:flex;gap:5px;font-family:"Montserrat",sans-serif;font-weight:700;font-size:4px;color:var(--white)}
.footer-bar{position:absolute;left:0;top:41px;width:412px;height:20px;background:var(--footer-deep);text-align:center;font-size:3.8px;line-height:20px;color:var(--white);font-weight:600}
.footer-bar span{color:var(--green)}
</style>
</head>
<body>
<div class="stage">
<div class="page">

  <header class="hero" role="img" aria-label="Large old tree with a wide green canopy">
    <div class="brand" style="left:38px;top:12px;font-size:6px"><i style="width:12px;height:12px"></i>Quillby Logistics</div>
    <nav class="nav"><span class="active">HOME</span><span>ABOUT</span><span>SERVICES</span><span>CAREERS</span><span>CONTACT</span><span>ENGLISH ▾</span></nav>
    <h1>Quillby Logistics – Sustainable Last Mile</h1>
    <p class="lead">Because we care about trees!</p>
    <div class="btn" style="left:45px;top:119px;width:61px;height:15px">GET STARTED</div>
    <svg class="arrow" style="left:11px" viewBox="0 0 17 17"><circle cx="8.5" cy="8.5" r="8.5" fill="#8a8a8a" opacity=".7"/><path d="M10 5 6.5 8.5 10 12" stroke="#fff" stroke-width="1.3" fill="none"/></svg>
    <svg class="arrow" style="left:383px" viewBox="0 0 17 17"><circle cx="8.5" cy="8.5" r="8.5" fill="#fff"/><path d="M7 5 10.5 8.5 7 12" stroke="#222" stroke-width="1.3" fill="none"/></svg>
    <svg class="abs" style="left:202px;top:180px" width="8" height="8" viewBox="0 0 8 8"><path d="M1 1 4 4 7 1M1 4 4 7 7 4" stroke="#fff" stroke-width="1" fill="none"/></svg>
  </header>

  <section class="about">
    <div class="abs about-photo" role="img" aria-label="Quiet country road lined by a single tree at sunrise"></div>
    <h2 class="section-title abs" style="left:238px;top:26px">ABOUT <span>US</span></h2>
    <div class="rule" style="left:238px;top:43px"></div>

    <div class="icon-ring line-icon" style="left:210px;top:89px"><svg width="10" height="8" viewBox="0 0 10 8"><rect x=".5" y="1" width="6" height="4.5" fill="none" stroke="#1f9a45" stroke-width=".7"/><path d="M6.5 2.5h2l1 1.5v1.5h-3" fill="none" stroke="#1f9a45" stroke-width=".7"/><circle cx="2.5" cy="6.5" r="1" fill="#1f9a45"/><circle cx="7.5" cy="6.5" r="1" fill="#1f9a45"/></svg></div>
    <div class="abs about-item tiny" style="left:238px;top:54px;width:138px">
      <h3>Who We Are</h3>
      <p>Quillby Logistics is a pioneer in urban green logistics and provides zero-emissions last mile delivery services for its logistics and retail clients.</p>
      <p>We take on urban parcel delivery for our clients with a 100% electric commercial vehicles fleet, fair and sustainable working conditions for our employees and an unparalleled professional and customer-focused mindset.</p>
    </div>

    <div class="icon-ring line-icon" style="left:211px;top:174px"><svg width="8" height="8" viewBox="0 0 8 8"><rect x="1" y="1" width="6" height="6" fill="none" stroke="#1f9a45" stroke-width=".7"/><path d="M4 1v6M1 4h6" stroke="#1f9a45" stroke-width=".7"/></svg></div>
    <div class="abs about-item tiny" style="left:238px;top:138px;width:138px">
      <h3>Our Mission</h3>
      <p>To satisfy consumers' ever-rising desire to buy products online, the CO2 emissions from delivery traffic will increase by 32% in the top 100 cities globally until 2030.</p>
      <p>Our clients care about our planet the same way we do, which is why Quillby Logistics helps to make the planet a better place by running the most environmentally friendly urban last mile possible.</p>
    </div>

    <div class="icon-ring line-icon" style="left:210px;top:255px"><svg width="8" height="8" viewBox="0 0 8 8"><rect x="1" y="1" width="5" height="6" fill="none" stroke="#1f9a45" stroke-width=".7"/><circle cx="6" cy="5.5" r="1.5" fill="#1f9a45"/></svg></div>
    <div class="abs about-item tiny" style="left:238px;top:219px;width:138px">
      <h3>Our Values</h3>
      <p>We see ourselves as a professional services company who strongly cares about the environment, its clients and their customers, as well as its employees.</p>
      <p>We believe that delivering parcels with zero emissions and providing a unique customer experience through a highly professional attitude and a great team spirit are the cornerstones for Quillby Logistics to operate in today's world in a sustainable yet profitable way.</p>
    </div>
  </section>

  <section class="compare">
    <h2>Quillby Logistics is...</h2>
    <div class="icon-ring fill-ring" style="left:175px;top:40px"><svg width="12" height="9" viewBox="0 0 12 9"><rect x=".5" y=".5" width="7" height="5.5" fill="none" stroke="#fff" stroke-width=".8"/><path d="M7.5 2.5h2.5l1.5 2v2h-4" fill="none" stroke="#fff" stroke-width=".8"/><circle cx="3" cy="7.5" r="1" fill="#fff"/><circle cx="9" cy="7.5" r="1" fill="#fff"/></svg></div>
    <div class="icon-ring fill-ring" style="left:211px;top:40px"><svg width="10" height="10" viewBox="0 0 10 10"><rect x="1" y="1" width="6" height="8" fill="none" stroke="#fff" stroke-width=".8"/><path d="M3 3.5 6 5 3 6.5z" fill="#fff"/></svg></div>
    <ul class="not-list">
      <li>an ordinary parcel delivery firm</li>
      <li>polluting our cities</li>
      <li>Always in a rush</li>
      <li>short-term oriented focusing on profit only</li>
      <li>yet another parcel delivery firm</li>
    </ul>
    <div class="divider"></div>
    <ul class="is-list">
      <li>a pioneering green last mile delivering parcels emissions-free putting</li>
      <li>customer experience first</li>
      <li>operating the business sustainably</li>
      <li>focusing on the environment, customers and employees</li>
      <li>a professional services company</li>
    </ul>
  </section>

  <section class="services">
    <div class="abs leaves" style="left:0;top:0;width:130px;height:50px" role="img" aria-label="Green leaves hanging from the top left corner"></div>
    <div class="abs leaves" style="right:0;top:0;width:126px;height:60px;background:linear-gradient(200deg,#2f7a2a,#5aa63a 60%,rgba(255,255,255,0))" role="img" aria-label="Green leaves hanging from the top right corner"></div>
    <h2 class="section-title abs" style="left:0;width:412px;text-align:center;top:31px">OUR <span>SERVICES</span></h2>
    <div class="rule" style="left:198px;top:48px"></div>
    <p class="tiny abs" style="left:90px;top:58px;width:232px;text-align:center">Quillby Logistics provides last mile delivery services in urban areas to clients in the logistics and retail space. Our permanent employees are all highly trained and commit to highest professional standards which we continuously review and further develop with them.</p>

    <div class="card" style="left:38px"><div class="icon-ring"><svg width="9" height="9" viewBox="0 0 9 9"><circle cx="4.5" cy="4.5" r="3.5" fill="none" stroke="#fff" stroke-width=".8"/><path d="M3.5 3 5.5 4.5 3.5 6z" fill="#fff"/></svg></div><h4>ZERO-EMISSION DELIVERY</h4><p>We operate a 100% electric commercial vehicle fleet</p></div>
    <div class="card" style="left:124px"><div class="icon-ring"><svg width="9" height="9" viewBox="0 0 9 9"><circle cx="4.5" cy="2.5" r="1.6" fill="#fff"/><path d="M1.5 8.5c0-2.5 1.3-3.5 3-3.5s3 1 3 3.5z" fill="#fff"/></svg></div><h4>HIGHLY TRAINED DELIVERY DRIVERS</h4><p>We only employ permanently, train far above average, and live a great team spirit</p></div>
    <div class="card" style="left:210px"><div class="icon-ring"><svg width="9" height="9" viewBox="0 0 9 9"><path d="M4.5 .8 5.6 3.3 8.3 3.5 6.2 5.2 6.9 8 4.5 6.5 2.1 8 2.8 5.2.7 3.5 3.4 3.3z" fill="none" stroke="#fff" stroke-width=".7"/></svg></div><h4>PROFESSIONAL ALL AROUND</h4><p>We honor our commitments and hold ourselves to the highest professional standards</p></div>
    <div class="card" style="left:296px"><div class="icon-ring"><svg width="9" height="9" viewBox="0 0 9 9"><circle cx="4.5" cy="4.5" r="3.5" fill="none" stroke="#fff" stroke-width=".8"/><circle cx="4.5" cy="4.5" r="1.3" fill="#fff"/></svg></div><h4>UNPARALLELED CUSTOMER FOCUS</h4><p>We live a customer-oriented mindset, always measuring ourselves against their experience</p></div>
  </section>

  <section class="touch" role="img" aria-label="Dark green fern leaves">
    <h2 class="cta-title" style="left:70px;top:27px">Get in touch with Quillby Logistics</h2>
    <p class="cta-text" style="left:70px;top:43px;width:262px">If you got excited, or have a question about our services, our approach, our jobs or just want to get in touch to chat about how green logistics can make the planet a little bit better, please get in touch!</p>
    <div class="btn" style="left:71px;top:76px;width:49px;height:12px">CONTACT US</div>
  </section>

  <section class="careers">
    <h2 class="section-title abs" style="left:38px;top:17px">OUR <span>CAREERS</span></h2>
    <div class="rule" style="left:38px;top:34px"></div>
    <div class="abs careers-text" style="left:38px;top:44px;width:150px">
      <p>If you join Quillby Logistics, you join a family. We elevate one another, care for each other's wellbeing and growth, and celebrate our successes. We strongly believe growth is a team sport and that every member of the family fully contributes to the achievements of the company overall.</p>
      <p>At the heart of everything we do at Quillby Logistics is a relentless focus on our mission. That's why we aim to ensure our employees can follow their own passion at the workplace, be this working in a truly collaborative and caring team, putting a smile on a customer's face or making the world a better place. While we are helping our clients grow by delivering their parcels, we are also helping all our employees grow personally and professionally. We care about our employees' happiness and wellbeing which is why we provide additional benefits like supplementary health insurance.</p>
      <p>If you are excited about joining our Quillby Logistics family, please check out our open positions.</p>
    </div>
    <div class="abs careers-photo" role="img" aria-label="Delivery driver in a blue uniform holding a parcel in front of a van"></div>

    <div class="abs accordion">
      <div class="acc-head"><span>FULL-TIME DRIVER / PARCEL DELIVERER (M/F/D) FOR BERLIN</span><span>−</span></div>
      <div class="acc-box" style="top:29px;height:112px">
        <div class="acc-row" style="border-bottom:.8px solid #7fc596;padding:0 19px"><span>Your tasks as a delivery driver</span><b>−</b></div>
        <div class="acc-body">
          <p>- Delivery of packages to end customers</p>
          <p>- In the delivery center: preparation of the tour and loading of the delivery van with parcels</p>
          <p>- Drive from the delivery center to the delivery area - you will be guided by a navigation system</p>
          <p>- Delivery of the parcels to end customers in the delivery area - the navigation helps you here too - Suggest ideas for improvement in the delivery process</p>
          <p>- Take care of and charge the delivery van</p>
        </div>
      </div>
      <div class="acc-box acc-row" style="top:151px">Required knowledge and skills<b>+</b></div>
      <div class="acc-box acc-row" style="top:179px">What you can expected from the Quillby Logistics family<b>+</b></div>
    </div>
  </section>

  <section class="interest" role="img" aria-label="Close-up of a bright green leaf">
    <h2 class="cta-title" style="left:66px;top:24px">Interested? Send us an email or give us a call.</h2>
    <p class="cta-text" style="left:67px;top:40px;width:280px">We offer a secure and varied job in a rapidly growing company with opportunities for advancement. We would like to invite you to a trial day.</p>
    <div class="btn" style="left:68px;top:66px;width:49px;height:12px">CONTACT US</div>
  </section>

  <section class="contact">
    <h2 class="section-title abs" style="left:38px;top:38px">CONTACT <span>US</span></h2>
    <div class="rule" style="left:38px;top:55px"></div>
    <p class="abs" style="left:38px;top:63px;width:290px;font-size:4.4px;line-height:8px;color:var(--ink)">We'd love to hear from you!<br><br>Whether you have a question about our services, our approach, our jobs or just want to get in touch to chat about how green logistics can make the planet a little bit better, our team is ready to answer your questions and enquiries.</p>
    <span class="field-label" style="top:115px">Name</span>
    <div class="field" style="top:122px;width:77px;height:13px"></div>
    <span class="field-label" style="top:144px">Subject</span>
    <div class="field" style="top:151px;width:106px;height:13px"></div>
    <span class="field-label" style="top:173px">Message</span>
    <div class="field" style="top:180px;width:134px;height:57px"></div>
    <div class="btn" style="left:38px;top:245px;width:50px;height:14px;box-shadow:0 1px 3px rgba(0,0,0,.2)">CONTACT US</div>

    <div class="info" style="top:115px"><svg width="6" height="7" viewBox="0 0 6 7"><path d="M3 7C1 4.6 0 3.3 0 2.2A3 3 0 0 1 6 2.2C6 3.3 5 4.6 3 7z" fill="#1f9a45"/><circle cx="3" cy="2.3" r="1" fill="#fff"/></svg>48 Linden Row, Portfield, PF 20417</div>
    <div class="info" style="top:128px"><svg width="7" height="5" viewBox="0 0 7 5"><rect width="7" height="5" fill="#1f9a45"/><path d="M0 0 3.5 2.8 7 0" stroke="#fff" stroke-width=".6" fill="none"/></svg>hello@quillby.example</div>
    <div class="info" style="top:140px"><svg width="7" height="7" viewBox="0 0 7 7"><path d="M1.5.3 2.8 1.8 2 3a4.5 4.5 0 0 0 2 2l1.2-.8 1.5 1.3L6 6.6C3 6.8.2 4 .4 1z" fill="#1f9a45"/></svg>+1 555 014 2290</div>
  </section>

  <footer class="footer">
    <div class="brand" style="left:38px;top:13px;font-size:5px"><i style="width:10px;height:10px"></i>Quillby Logistics</div>
    <nav class="footer-nav"><span>HOME</span><span>|</span><span>ABOUT</span><span>|</span><span>SERVICES</span><span>|</span><span>CAREERS</span><span>|</span><span>CONTACT</span></nav>
    <div class="footer-bar">© 2020 Quillby Logistics. All Rights Deserved. <span>Legal Notice. Privacy Policy</span></div>
  </footer>

</div>
</div>
</body>
</html>
```